Tech business card design

We need an amazing business card design for our new business 'Brakka' a marketing tech startup based in Sydney, Australia. We provide an online marketplace for businesses to search and buy advertising media, connect with service providers and learn more about marketing. We wish to communicate 'cool tech', reliability and professionalism and design based around our logo.

Target Market(s)

Business Owners

Contact Information for Business Card

Name
Position
Email Address
Website
Phone Number

Font styles to use
Other font styles liked:
• Avenir & Avenir Next

Colors

Designer to choose colors to be used in the design.

```html
<!DOCTYPE html>
<html lang="en">
<head>
<meta charset="UTF-8">
<title>Brakka Business Card</title>
<link href="https://fonts.googleapis.com/css2?family=Mulish:wght@400;500;800&display=swap" rel="stylesheet">
<style>
  :root {
    --stage: #3a3a3c;
    --navy: #0f1036;
    --navy-deep: #07071c;
    --glow: #2a2a8a;
    --ink: #ffffff;
    --ink-soft: #d9dbf0;
    --rule: #8f92c9;
  }
  * { box-sizing: border-box; margin: 0; padding: 0; }
  html, body {
    width: 1200px; height: 1000px; overflow: hidden;
    background: var(--stage);
    font-family: "Mulish", sans-serif;
  }
  .canvas { position: relative; width: 1200px; height: 1000px; }
  .card {
    position: absolute; left: 220px; width: 760px; height: 434px;
    border-radius: 24px; overflow: hidden;
    box-shadow: 0 18px 40px rgba(0,0,0,.45);
  }
  .card--front { top: 50px; background: var(--navy-deep); }
  .card--back { top: 516px; background: var(--navy); }

  .front-art {
    position: absolute; inset: 0;
    background: radial-gradient(ellipse at 55% 45%, var(--glow) 0%, #14145a 30%, var(--navy-deep) 75%);
  }
  .wordmark {
    font-weight: 800; color: var(--ink); letter-spacing: -2px; line-height: 1;
  }
  .card--front .wordmark {
    position: absolute; left: 0; right: 0; top: 150px;
    text-align: center; font-size: 130px;
  }
  .card--back .wordmark {
    position: absolute; left: 48px; top: 34px; font-size: 112px;
  }
  .contact { position: absolute; left: 52px; top: 212px; color: var(--ink); }
  .contact__name { font-size: 30px; font-weight: 500; }
  .contact__role { font-size: 17px; color: var(--ink-soft); margin-top: 2px; }
  .contact__list { list-style: none; margin-top: 22px; }
  .contact__item {
    display: flex; align-items: center; gap: 12px;
    font-size: 19px; margin-bottom: 10px;
  }
  .contact__item svg { width: 18px; height: 18px; fill: var(--ink-soft); }
  .footer-rule {
    position: absolute; left: 0; right: 0; bottom: 54px;
    display: flex; align-items: center; gap: 14px;
  }
  .footer-rule__line { height: 1px; background: var(--rule); }
  .footer-rule__line--long { flex: 1; }
  .footer-rule__line--short { width: 48px; }
  .footer-rule__web { color: var(--ink); font-size: 19px; letter-spacing: .5px; }
</style>
</head>
<body>
<main class="canvas">
  <section class="card card--front">
    <div class="front-art" role="img" aria-label="Abstract blue circuit-board and light-streak tech texture"></div>
    <div class="wordmark">brakka</div>
  </section>

  <section class="card card--back">
    <div class="wordmark">brakka</div>
    <div class="contact">
      <div class="contact__name">Marcus Vale</div>
      <div class="contact__role">Managing Director</div>
      <ul class="contact__list">
        <li class="contact__item">
          <svg viewBox="0 0 24 24" aria-hidden="true"><path d="M6.6 10.8a15.1 15.1 0 0 0 6.6 6.6l2.2-2.2a1 1 0 0 1 1-.25 11.4 11.4 0 0 0 3.6.57 1 1 0 0 1 1 1V20a1 1 0 0 1-1 1A17 17 0 0 1 3 4a1 1 0 0 1 1-1h3.5a1 1 0 0 1 1 1c0 1.25.2 2.45.57 3.57a1 1 0 0 1-.25 1z"/></svg>
          800-214-0376
        </li>
        <li class="contact__item">
          <svg viewBox="0 0 24 24" aria-hidden="true"><path d="M3 5h18a1 1 0 0 1 1 1v12a1 1 0 0 1-1 1H3a1 1 0 0 1-1-1V6a1 1 0 0 1 1-1zm1 2.3V17h16V7.3l-8 5.2z"/></svg>
          marcusv@brakkamail.com
        </li>
      </ul>
    </div>
    <div class="footer-rule">
      <span class="footer-rule__line footer-rule__line--long"></span>
      <span class="footer-rule__web">www.brakka.com</span>
      <span class="footer-rule__line footer-rule__line--short"></span>
    </div>
  </section>
</main>
</body>
</html>
```